Penny auction website for high end market

need a penny auction web design , requirement as below :-

- classy and noble, as i am only selli high end products
- 25 products for the main page , 5 products per row ( please see sample picture )
- top 5 products can be highlighted as those are limited edition products
- main page , products page, members page , faq and about us page
- matching logo with the name lotvo
- clean
- responsive for desktoop
-mobile version
Updates

i missed the mobile version, i should get the mobile version aswell, for desktop it should be responsive Added Wednesday, August 16, 2017

designer may use gold or silver color too as i am selling only high end products exclusively for members only, the layout can be different than the sample, it just a guide line for the sample, other better layout would be great to see and to have.

some idea how highend feel to me https://img.kravenstock.example/scr/51200/shimmering-gem-layout-template_51277-original.jpg

guys, please use this design https://www.layoutquarry.example/site-templates/51277.html as the base , i want it high class and up market, thanks

Target Market(s)

highend products buyer

Number of Pages Required

5+ page

Font styles to use
Serif
Sans Serif
Script
Other font styles liked:
• designer match it

Colors

Designer to choose colors to be used in the design.

Requirements
Must have
• source code, logos ( use lotvo for now, will change later when confirm ) , PSD
Nice to have
• more different type of designs would be great, designers can present they ideas other than my requirement

```html
<!DOCTYPE html>
<html lang="en">
<head>
<meta charset="utf-8">
<title>lotvo — Penny Auctions</title>
<link rel="stylesheet" href="https://fonts.googleapis.com/css2?family=Nunito:wght@400;600;700;800;900&family=Open+Sans:wght@400;600&display=swap">
<style>
:root{
  --yellow:#ffd400;
  --yellow-deep:#f5c400;
  --ink:#1e1e1e;
  --text:#555;
  --muted:#8a8a8a;
  --line:#e6e6e6;
  --panel:#f1f1f1;
  --white:#fff;
}
*{box-sizing:border-box;margin:0;padding:0}
html,body{width:1200px;height:3896px;overflow:hidden;background:var(--white)}
body{font-family:"Open Sans",sans-serif;color:var(--text);position:relative}
.heading{font-family:"Nunito",sans-serif;color:var(--ink)}
.btn{display:inline-block;background:var(--yellow);color:var(--ink);font-family:"Nunito",sans-serif;font-weight:800;font-size:13px;border-radius:20px;padding:9px 26px}
.btn-small{font-size:10px;padding:5px 16px}

/* top bar */
.topbar{height:24px;border-bottom:1px solid var(--line);display:flex;align-items:center;justify-content:space-between;padding:0 176px;font-size:10px;color:var(--muted)}
.topbar .social{display:flex;gap:6px;align-items:center}
.dot{width:9px;height:9px;border-radius:50%;background:#b9b9b9;display:inline-block}

/* nav */
.nav{height:64px;display:flex;align-items:center;justify-content:space-between;padding:0 176px}
.brand{font-family:"Nunito",sans-serif;font-weight:900;font-size:30px;color:var(--ink);display:flex;align-items:center;gap:8px}
.brand-mark{width:12px;height:12px;background:var(--yellow);border-radius:50%}
.menu{display:flex;gap:22px;font-size:12px;color:var(--ink);align-items:center}
.menu .active{background:var(--yellow);padding:4px 10px;border-radius:12px}
.search{display:flex;align-items:center;gap:6px;color:var(--muted);font-size:11px}

/* hero */
.hero{position:absolute;top:88px;left:0;width:1200px;height:512px;background:linear-gradient(90deg,#f6f6f6,#ececec)}
.hero-copy{position:absolute;left:220px;top:110px;width:360px}
.hero-tag{display:inline-block;background:var(--yellow);padding:8px 22px;font-family:"Nunito",sans-serif;font-weight:900;font-size:44px;color:var(--ink);line-height:1}
.hero-sub{font-family:"Nunito",sans-serif;font-weight:800;font-size:38px;color:var(--ink);margin-top:10px}
.hero-copy p{font-size:13px;line-height:1.5;margin:10px 0 28px;color:#555}
.hero-photo{position:absolute;right:0;top:0;width:560px;height:512px;background:linear-gradient(135deg,#c34d4d 0%,#6f3535 30%,#e7e3df 45%,#d58a3b 60%,#3f6a8f 100%)}

/* about */
.about{position:absolute;top:600px;left:0;width:1200px;height:640px;text-align:center}
.about h2{font-size:44px;font-weight:900;padding-top:56px}
.about p{width:560px;margin:22px auto 30px;font-size:11px;line-height:1.7;color:var(--muted)}
.about-photo{position:absolute;left:360px;top:340px;width:480px;height:260px;border-radius:8px;background:linear-gradient(90deg,#ffd400,#ff4b2b,#9b2cf0,#2ad1ff,#2dd46b,#ffd400)}

/* products */
.products{position:absolute;top:1280px;left:0;width:1200px;text-align:center}
.eyebrow{font-family:"Nunito",sans-serif;font-weight:800;font-size:20px;color:var(--ink)}
.products h2{font-size:60px;font-weight:900;line-height:1;margin-bottom:36px}
.grid{width:752px;margin:0 auto;display:grid;grid-template-columns:repeat(4,1fr);gap:14px 10px}
.card{height:310px;border:1px solid var(--line);background:var(--white);padding-bottom:14px}
.card-photo{height:150px;margin:8px;background:linear-gradient(180deg,#f2f2f2,#dcdcdc)}
.card-name{font-family:"Nunito",sans-serif;font-weight:800;font-size:13px;color:var(--ink);margin-top:10px}
.card-meta{font-size:10px;color:var(--muted);line-height:1.6;margin:4px 0 10px}
.card-price{font-weight:600;color:var(--ink);font-size:12px}

/* offer band */
.offer{position:absolute;top:2428px;left:0;width:1200px;height:332px;background:var(--yellow)}
.offer-photo{position:absolute;left:0;top:0;width:560px;height:332px;background:linear-gradient(135deg,#f4f4f4,#cfcfcf 55%,#6a6a6a)}
.offer-copy{position:absolute;left:640px;top:50px;width:320px}
.offer-copy h3{font-size:52px;font-weight:900}
.offer-copy p{font-size:11px;line-height:1.6;color:#4a4a00;margin:8px 0 18px}
.countdown{display:flex;gap:22px;margin-bottom:20px}
.count b{display:block;font-family:"Nunito",sans-serif;font-weight:900;font-size:30px;color:var(--ink);line-height:1}
.count span{font-size:9px;color:var(--ink)}
.btn-dark{background:var(--ink);color:var(--white)}

/* promos */
.promos{position:absolute;top:2840px;left:248px;width:752px;height:340px;display:flex;gap:8px}
.promo{flex:1;background:var(--panel);position:relative;padding:80px 0 0 26px}
.promo h4{font-family:"Nunito",sans-serif;font-weight:900;font-size:18px;color:var(--ink)}
.promo .big{font-family:"Nunito",sans-serif;font-weight:800;font-size:24px;color:var(--ink);margin-bottom:20px}
.promo-photo{position:absolute;right:24px;top:30px;width:150px;height:280px;border-radius:6px}
.watch{background:linear-gradient(180deg,#8b5a34,#d9c29a 50%,#6b3f21)}
.phone{background:linear-gradient(180deg,#3b4f78,#9ab3d6 50%,#1c2a44);width:110px;right:40px}

/* newsletter */
.newsletter{position:absolute;top:3220px;left:0;width:1200px;height:180px;background:var(--yellow);text-align:center;padding-top:34px}
.newsletter h2{font-size:36px;font-weight:900}
.newsletter p{font-size:12px;color:#4a4a00;margin:4px 0 18px}
.signup{width:520px;height:40px;margin:0 auto;background:var(--white);border-radius:20px;display:flex;align-items:center;justify-content:space-between;padding-left:20px;font-size:11px;color:var(--muted)}
.signup .btn{background:var(--ink);color:var(--white);padding:12px 30px}

/* footer */
.follow{position:absolute;top:3440px;left:0;width:1200px;display:flex;justify-content:center;gap:12px}
.follow i{width:42px;height:42px;border:2px solid var(--ink);border-radius:50%}
.footer-cols{position:absolute;top:3520px;left:248px;width:752px;display:grid;grid-template-columns:repeat(4,1fr);gap:20px}
.footer-cols h5{font-family:"Nunito",sans-serif;font-weight:800;font-size:16px;color:var(--ink);border-bottom:2px solid var(--yellow);display:inline-block;padding-bottom:4px;margin-bottom:12px}
.footer-cols li{list-style:none;font-size:10px;color:var(--muted);line-height:2.1}
.footer-links{position:absolute;top:3775px;left:0;width:1200px;display:flex;justify-content:center;gap:14px;font-size:9px;color:var(--muted);border-top:1px solid var(--line);padding-top:14px}
.bottombar{position:absolute;top:3862px;left:0;width:1200px;height:34px;background:var(--yellow);display:flex;align-items:center;justify-content:center;font-size:10px;color:var(--ink)}
</style>
</head>
<body>

<div class="topbar">
  <div class="social"><i class="dot"></i><i class="dot"></i><i class="dot"></i><i class="dot"></i><span>Phone: +1 555 014 2280</span></div>
  <div>Login / Register</div>
</div>

<header class="nav">
  <div class="brand"><span class="brand-mark"></span>lotvo</div>
  <nav class="menu">
    <span>Home</span><span>About us</span><span>Products</span><span>Members</span><span>Faq</span><span class="active">Contact us</span>
    <span class="search">
      <svg width="12" height="12" viewBox="0 0 12 12"><circle cx="5" cy="5" r="3.8" fill="none" stroke="#1e1e1e" stroke-width="1.5"/><line x1="8" y1="8" x2="11" y2="11" stroke="#1e1e1e" stroke-width="1.5"/></svg>Search
    </span>
  </nav>
</header>

<section class="hero">
  <div class="hero-copy">
    <div class="hero-tag heading">COLLECTIONS 2017</div>
    <div class="hero-sub">UP TO 50% SALES</div>
    <p>Lorem Ipsum is simply dummy text of the printing and typesetting industry.</p>
    <span class="btn">Bid Now</span>
  </div>
  <div class="hero-photo" role="img" aria-label="Flat lay of suede shoes, a checked shirt and folded denim jeans"></div>
</section>

<section class="about">
  <h2 class="heading">ABOUT LOTVO</h2>
  <p>Lorem Ipsum is simply dummy text of the printing and typesetting industry. Lorem Ipsum has been the industry's standard dummy text ever since the 1500s, when an unknown printer took a galley of type and scrambled it to make a type specimen book. It has survived not only five centuries but also the leap into electronic typesetting, remaining essentially unchanged.</p>
  <span class="btn">Read More</span>
  <div class="about-photo" role="img" aria-label="Row of colourful smartphones fanned out side by side"></div>
</section>

<section class="products">
  <div class="eyebrow">LIMITED EDITION</div>
  <h2 class="heading">PRODUCTS</h2>
  <div class="grid">
    <div class="card"><div class="card-photo" role="img" aria-label="Laptop"></div><div class="card-name">Sorvane laptop</div><div class="card-meta">12:00:25<br>Random Bidder<br><span class="card-price">$149.00</span></div><span class="btn btn-small">Bid Now</span></div>
    <div class="card"><div class="card-photo" role="img" aria-label="DSLR camera"></div><div class="card-name">Kellon Lux 700D</div><div class="card-meta">12:00:25<br>Random Bidder<br><span class="card-price">$149.00</span></div><span class="btn btn-small">Bid Now</span></div>
    <div class="card"><div class="card-photo" role="img" aria-label="Smartphone"></div><div class="card-name">Sorvane Mobile</div><div class="card-meta">12:00:25<br>Random Bidder<br><span class="card-price">$149.00</span></div><span class="btn btn-small">Bid Now</span></div>
    <div class="card"><div class="card-photo" role="img" aria-label="Tablet"></div><div class="card-name">Aria Pad</div><div class="card-meta">12:00:25<br>Random Bidder<br><span class="card-price">$149.00</span></div><span class="btn btn-small">Bid Now</span></div>

    <div class="card"><div class="card-photo" role="img" aria-label="Leather shoes"></div><div class="card-name">Shoes</div><div class="card-meta">12:00:25<br>Random Bidder<br><span class="card-price">$14.00</span></div><span class="btn btn-small">Bid Now</span></div>
    <div class="card"><div class="card-photo" role="img" aria-label="Denim jeans"></div><div class="card-name">Men Pant</div><div class="card-meta">12:00:25<br>Random Bidder<br><span class="card-price">$109.00</span></div><span class="btn btn-small">Bid Now</span></div>
    <div class="card"><div class="card-photo" role="img" aria-label="Wrist watch"></div><div class="card-name">Men Watch</div><div class="card-meta">12:00:25<br>Random Bidder<br><span class="card-price">$34.00</span></div><span class="btn btn-small">Bid Now</span></div>
    <div class="card"><div class="card-photo" role="img" aria-label="Perfume bottle"></div><div class="card-name">Perfume</div><div class="card-meta">12:00:25<br>Random Bidder<br><span class="card-price">$109.00</span></div><span class="btn btn-small">Bid Now</span></div>

    <div class="card"><div class="card-photo" role="img" aria-label="Laptop"></div><div class="card-name">Sorvane laptop</div><div class="card-meta">12:00:25<br>Random Bidder<br><span class="card-price">$149.00</span></div><span class="btn btn-small">Bid Now</span></div>
    <div class="card"><div class="card-photo" role="img" aria-label="DSLR camera"></div><div class="card-name">Kellon Lux 700D</div><div class="card-meta">12:00:25<br>Random Bidder<br><span class="card-price">$149.00</span></div><span class="btn btn-small">Bid Now</span></div>
    <div class="card"><div class="card-photo" role="img" aria-label="Smartphone"></div><div class="card-name">Sorvane Mobile</div><div class="card-meta">12:00:25<br>Random Bidder<br><span class="card-price">$149.00</span></div><span class="btn btn-small">Bid Now</span></div>
    <div class="card"><div class="card-photo" role="img" aria-label="Tablet"></div><div class="card-name">Aria Pad</div><div class="card-meta">12:00:25<br>Random Bidder<br><span class="card-price">$149.00</span></div><span class="btn btn-small">Bid Now</span></div>
  </div>
</section>

<section class="offer">
  <div class="offer-photo" role="img" aria-label="Vintage camera on a yellow backdrop"></div>
  <div class="offer-copy">
    <h3 class="heading">25% Off</h3>
    <p>Lorem Ipsum is simply dummy text of the printing and typesetting industry. Lorem Ipsum has been the standard dummy text ever since.</p>
    <div class="countdown">
      <div class="count"><b>13</b><span>Days</span></div>
      <div class="count"><b>20</b><span>Hours</span></div>
      <div class="count"><b>18</b><span>Mins</span></div>
      <div class="count"><b>54</b><span>Secs</span></div>
    </div>
    <span class="btn btn-dark">Bid Now</span>
  </div>
</section>

<section class="promos">
  <div class="promo">
    <h4>SMART PHONE</h4><div class="big">Up to 50%</div><span class="btn btn-small">Bid Now</span>
    <div class="promo-photo watch" role="img" aria-label="Leather strap wrist watch"></div>
  </div>
  <div class="promo">
    <h4>SMART PHONE</h4><div class="big">Up to 70%</div><span class="btn btn-small">Bid Now</span>
    <div class="promo-photo phone" role="img" aria-label="Smartphone standing upright"></div>
  </div>
</section>

<section class="newsletter">
  <h2 class="heading">SUBSCRIBE TO NEWSLETTER</h2>
  <p>Lorem Ipsum is simply dummy text of the printing and typesetting industry.</p>
  <div class="signup"><span>Your Email Address</span><span class="btn">SUBSCRIBE</span></div>
</section>

<div class="follow"><i></i><i></i><i></i><i></i><i></i></div>

<footer class="footer-cols">
  <div><h5>Contact us</h5><ul><li>Phone: +1 555 014 2280</li><li>Email: hello@lotvo.example</li><li>Address: 48 Harbour Lane, Suite 12</li><li>Westfield, NY 10021</li></ul></div>
  <div><h5>My Account</h5><ul><li>Cart</li><li>Checkout</li><li>Wishlist</li><li>Terms &amp; Policy</li><li>My Account</li><li>Returns</li></ul></div>
  <div><h5>Infomation</h5><ul><li>Shipping &amp; Returns</li><li>Sitemap</li><li>Trade In Order</li><li>Privacy Notice</li><li>Store Locator</li><li>Gift Cards</li></ul></div>
  <div><h5>How to Buy</h5><ul><li>Making Payments</li><li>Delivery Options</li><li>Buyer Protection</li><li>New User Guide</li><li>Bid Credits</li><li>Help Center</li></ul></div>
</footer>

<div class="footer-links"><span>Accessories</span><span>Audio</span><span>Batteries</span><span>Camera</span><span>Computer</span><span>Desktop Security</span><span>Headsets</span><span>Laptop</span><span>Lenses</span><span>Phones</span><span>Tablets</span><span>Watches</span></div>

<div class="bottombar">Copyright © 2017 lotvo. All rights reserved.</div>

</body>
</html>
```